Total Health and Wellness Infographic

Hello,
We need an infographic of the 16 factors for total health and wellness.  We are imagining a circle pie chart with all 16 categories, with each pie having a corresponding graphic in it.
We want it to be modern, beautiful, easy to understand (we welcome cartoon graphics)
The 16 points are:
a. Sleep
b. Exercise/Movement
c. Macronutrient Diet
d. Micronutrients
e. Health Habits (Tracking, Morning Routines, Mindfulness/Meditation)
f. CV Health
g. GI Health
h. Brain Health
i. Inflammation (Food allergies, etc)
j. Hormone Health
k. Stress
l. Immunity and Cancer Detection/ Prevention
m. Detoxification – heavy metals, pesticides, your environment
n. Longevity
o. Sexual Health
p. Aesthetics – Facial, Hair, Body
Attached are our brand standards for reference.
Let us know if you have any questions.
Thank you!

```html
<!DOCTYPE html>
<html lang="en">
<head>
<meta charset="utf-8">
<title>Vitalis Health – 16 Factors of Total Wellness</title>
<link href="https://fonts.googleapis.com/css2?family=Nunito+Sans:wght@400;700&display=swap" rel="stylesheet">
<style>
  :root {
    --brand-blue: #1c5aa6;
    --bg-light: #ffffff;
    --bg-fade: #e6e7e8;
    --tile-edge: #e9eaeb;
    --label: #ffffff;

    --stress: #0357a6;
    --hormone: #1e88cc;
    --brain: #00a88f;
    --inflammation: #00b9ee;
    --cv: #82c341;
    --gi: #3eb54a;
    --micro: #f5d800;
    --routines: #bfd730;
    --sleep: #ec1c24;
    --macro: #fbad18;
    --exercise: #f37321;
    --aesthetics: #ec1770;
    --sexual: #ec1c8c;
    --longevity: #ad208e;
    --immunity: #2e3192;
    --detox: #7b2c91;
  }
  html, body {
    margin: 0;
    padding: 0;
    width: 1200px;
    height: 800px;
    overflow: hidden;
  }
  .canvas {
    width: 1200px;
    height: 800px;
    background: linear-gradient(90deg, var(--bg-light) 0%, var(--bg-light) 62%, var(--bg-fade) 100%);
    font-family: "Nunito Sans", Arial, sans-serif;
  }
  .canvas svg { display: block; }
  .brand-name {
    font-family: "Nunito Sans", Arial, sans-serif;
    font-weight: 400;
    font-size: 46px;
    letter-spacing: 1px;
    fill: var(--brand-blue);
  }
  .tile-shape { stroke: var(--tile-edge); stroke-width: 6; }
  .tile-core { fill: #ffffff; fill-opacity: 0.28; stroke: #ffffff; stroke-opacity: 0.35; stroke-width: 2; }
  .tile-label {
    fill: var(--label);
    font-family: "Nunito Sans", Arial, sans-serif;
    font-weight: 700;
    font-size: 14.5px;
    letter-spacing: 0.3px;
    text-anchor: middle;
  }
  .tile-label--small { font-size: 12.5px; }
  .tile--stress .tile-shape { fill: var(--stress); }
  .tile--hormone .tile-shape { fill: var(--hormone); }
  .tile--brain .tile-shape { fill: var(--brain); }
  .tile--inflammation .tile-shape { fill: var(--inflammation); }
  .tile--cv .tile-shape { fill: var(--cv); }
  .tile--gi .tile-shape { fill: var(--gi); }
  .tile--micro .tile-shape { fill: var(--micro); }
  .tile--routines .tile-shape { fill: var(--routines); }
  .tile--sleep .tile-shape { fill: var(--sleep); }
  .tile--macro .tile-shape { fill: var(--macro); }
  .tile--exercise .tile-shape { fill: var(--exercise); }
  .tile--aesthetics .tile-shape { fill: var(--aesthetics); }
  .tile--sexual .tile-shape { fill: var(--sexual); }
  .tile--longevity .tile-shape { fill: var(--longevity); }
  .tile--immunity .tile-shape { fill: var(--immunity); }
  .tile--detox .tile-shape { fill: var(--detox); }
</style>
</head>
<body>
<main class="canvas">
  <svg width="1200" height="800" viewBox="0 0 1491 994" xmlns="http://www.w3.org/2000/svg">
    <defs>
      <polygon id="hex-outer" points="-95,0 -47.5,-82.3 47.5,-82.3 95,0 47.5,82.3 -47.5,82.3"/>
      <polygon id="hex-inner" points="-52,0 -26,-45 26,-45 52,0 26,45 -26,45"/>
    </defs>

    <text class="brand-name" x="138" y="137">VITALIS HEALTH</text>

    <g class="tile tile--stress" transform="translate(270 497)">
      <use class="tile-shape" href="#hex-outer"/>
      <use class="tile-core" href="#hex-inner" role="img" aria-label="Icon: head with lightning bolt"/>
      <text class="tile-label" y="-56">STRESS</text>
    </g>

    <g class="tile tile--hormone" transform="translate(428 405)">
      <use class="tile-shape" href="#hex-outer"/>
      <use class="tile-core" href="#hex-inner" role="img" aria-label="Icon: molecule hexagons"/>
      <text class="tile-label" y="-56">HORMONE</text>
      <text class="tile-label" y="71">HEALTH</text>
    </g>

    <g class="tile tile--brain" transform="translate(428 589)">
      <use class="tile-shape" href="#hex-outer"/>
      <use class="tile-core" href="#hex-inner" role="img" aria-label="Icon: brain"/>
      <text class="tile-label" y="-56">BRAIN HEALTH</text>
    </g>

    <g class="tile tile--inflammation" transform="translate(586 313)">
      <use class="tile-shape" href="#hex-outer"/>
      <use class="tile-core" href="#hex-inner" role="img" aria-label="Icon: peanut, wheat and fish"/>
      <text class="tile-label" y="-55">INFLAMATION</text>
    </g>

    <g class="tile tile--cv" transform="translate(586 497)">
      <use class="tile-shape" href="#hex-outer"/>
      <use class="tile-core" href="#hex-inner" role="img" aria-label="Icon: heart with pulse line"/>
      <text class="tile-label" y="-56">CV HEALTH</text>
    </g>

    <g class="tile tile--gi" transform="translate(586 681)">
      <use class="tile-shape" href="#hex-outer"/>
      <use class="tile-core" href="#hex-inner" role="img" aria-label="Icon: stomach"/>
      <text class="tile-label" y="-57">GI HEALTH</text>
    </g>

    <g class="tile tile--micro" transform="translate(745 221)">
      <use class="tile-shape" href="#hex-outer"/>
      <use class="tile-core" href="#hex-inner" role="img" aria-label="Icon: supplement bottle, apple and carrot"/>
      <text class="tile-label tile-label--small" y="-55">MICRONUTRIENT</text>
      <text class="tile-label tile-label--small" y="69">DIET</text>
    </g>

    <g class="tile tile--routines" transform="translate(745 405)">
      <use class="tile-shape" href="#hex-outer"/>
      <use class="tile-core" href="#hex-inner" role="img" aria-label="Icon: clock"/>
      <text class="tile-label" y="-56">ROUTINES</text>
    </g>

    <g class="tile tile--sleep" transform="translate(745 589)">
      <use class="tile-shape" href="#hex-outer"/>
      <use class="tile-core" href="#hex-inner" role="img" aria-label="Icon: person sleeping in bed"/>
      <text class="tile-label" y="-56">SLEEP</text>
    </g>

    <g class="tile tile--macro" transform="translate(903 313)">
      <use class="tile-shape" href="#hex-outer"/>
      <use class="tile-core" href="#hex-inner" role="img" aria-label="Icon: bowl of food"/>
      <text class="tile-label tile-label--small" y="-55">MACRONUTRIENT</text>
      <text class="tile-label tile-label--small" y="69">DIET</text>
    </g>

    <g class="tile tile--exercise" transform="translate(903 497)">
      <use class="tile-shape" href="#hex-outer"/>
      <use class="tile-core" href="#hex-inner" role="img" aria-label="Icon: running figure"/>
      <text class="tile-label" y="-56">EXERCISE</text>
      <text class="tile-label" y="69">MOVEMENT</text>
    </g>

    <g class="tile tile--aesthetics" transform="translate(903 681)">
      <use class="tile-shape" href="#hex-outer"/>
      <use class="tile-core" href="#hex-inner" role="img" aria-label="Icon: profile with flowing hair"/>
      <text class="tile-label" y="-57">AESTHETICS</text>
      <text class="tile-label" y="69">HEALTH</text>
    </g>

    <g class="tile tile--sexual" transform="translate(1061 589)">
      <use class="tile-shape" href="#hex-outer"/>
      <use class="tile-core" href="#hex-inner" role="img" aria-label="Icon: male and female symbols"/>
      <text class="tile-label" y="-56">SEXUAL</text>
      <text class="tile-label" y="69">HEALTH</text>
    </g>

    <g class="tile tile--longevity" transform="translate(1061 773)">
      <use class="tile-shape" href="#hex-outer"/>
      <use class="tile-core" href="#hex-inner" role="img" aria-label="Icon: hourglass with heart"/>
      <text class="tile-label" y="-57">LONGEVITY</text>
    </g>

    <g class="tile tile--immunity" transform="translate(1220 497)">
      <use class="tile-shape" href="#hex-outer"/>
      <use class="tile-core" href="#hex-inner" role="img" aria-label="Icon: cancer sign"/>
      <text class="tile-label tile-label--small" y="-65">IMMUNITY &amp;</text>
      <text class="tile-label tile-label--small" y="-52">CANCER</text>
      <text class="tile-label tile-label--small" y="62">DETECTION/</text>
      <text class="tile-label tile-label--small" y="75">PREVENTION</text>
    </g>

    <g class="tile tile--detox" transform="translate(1220 681)">
      <use class="tile-shape" href="#hex-outer"/>
      <use class="tile-core" href="#hex-inner" role="img" aria-label="Icon: detox packet with leaf"/>
      <text class="tile-label tile-label--small" y="-57">DETOXIFICATION</text>
    </g>
  </svg>
</main>
</body>
</html>
```